Book Cover Design: M&A for Software & SaaS Companies

I'm a startup book publisher, preparing to publish my first eBook entitled:

Grooming Your Platform Firm Toward Purchase (title)
The Platform Harvest Manual for Owners, Treasurers and Directors to Lift Worth and Steer Deals (subtitle)

Style Goal:

Premium, corporate, high-value
Feels closer to:
Private equity
Investment banking
Strategy consulting
NOT “startup playful”

Use QLV cover calculator
Include:
Front cover
Spine
Back cover
Bleed (0.125”)

Final Front Cover Text (Approved Version)

Top (small):
A PRACTICAL M&A PLAYBOOK

Main Title:
Preparing a
Software Company
for Sale

Subtitle:
The Platform Harvest Manual
for Founders, CFOs & Boards

Bottom Hook:
Maximise Valuation. Navigate M&A.

Back Cover:

Header (Hook)

Is Your Software Company Ready for a High-Value Exit?

Opening Paragraph

Selling a software company is a high-stakes, complex process—one that can determine the financial outcome for founders, investors and stakeholders.

Yet most businesses enter a sale process underprepared, leaving millions in value on the table.

Positioning Paragraph

Grooming Your Platform Firm Toward Purchase is a practical, execution-focused playbook for founders, CFOs and boards navigating the M&A process.

It provides a clear framework to prepare your business, position it for buyers, and maximise valuation.

Bullet Points (Key Outcomes)

Inside, you’ll learn how to:

✔ Maximise Valuation
Optimise financials, KPIs and growth narrative to attract premium offers

✔ Prepare for Due Diligence
Avoid the most common issues that derail deals

✔ Navigate the M&A Process
Understand buyers, advisors and deal dynamics

✔ Position for Private Equity & Strategic Buyers
Align your business with what acquirers actually value

Closing Statement

Whether you’re planning an exit in 12 months or 3 years, this book provides the structure and insight needed to achieve a successful outcome.

Footer

Author Name
Website (optional)

[Barcode space bottom right]

```html
<!DOCTYPE html>
<html lang="en">
<head>
<meta charset="utf-8">
<title>Grooming Your Platform Firm Toward Purchase – Cover Wrap</title>
<link rel="stylesheet" href="https://fonts.googleapis.com/css2?family=Barlow+Condensed:wght@400;500;600;700&family=Poppins:ital,wght@0,400;0,500;0,600;0,700;1,400&display=swap">
<style>
  :root {
    --page: #ffffff;
    --navy-deep: #0d1328;
    --navy: #16213f;
    --navy-mid: #1f2d52;
    --gold: #e9bf22;
    --gold-soft: #f1cf5a;
    --gold-line: #b89335;
    --amber-glow: rgba(150, 85, 25, 0.45);
    --white: #ffffff;
    --text: #eef0f5;
  }
  * { box-sizing: border-box; margin: 0; padding: 0; }
  html, body {
    width: 1200px; height: 865px; overflow: hidden;
    background: var(--page);
  }
  .wrap {
    position: absolute; left: 183px; top: 150px;
    width: 836px; height: 603px;
    display: flex;
  }

  /* ---------- Back cover ---------- */
  .back {
    position: relative; width: 404px; height: 100%;
    background:
      radial-gradient(ellipse 55% 35% at 62% 50%, var(--amber-glow), transparent 70%),
      radial-gradient(ellipse 40% 25% at 30% 40%, rgba(120,70,30,0.25), transparent 70%),
      linear-gradient(180deg, #0d1024 0%, #120f1e 55%, #0a0c18 100%);
    color: var(--text);
    font-family: 'Poppins', sans-serif;
  }
  .back-headline {
    position: absolute; top: 26px; left: 0; width: 100%;
    text-align: center;
    font-family: 'Barlow Condensed', sans-serif;
    text-transform: uppercase; line-height: 1;
  }
  .back-headline .line-one { font-size: 30px; font-weight: 600; color: var(--white); }
  .back-headline .line-two { font-size: 23px; font-weight: 400; color: var(--white); margin-top: 7px; }
  .accent { color: var(--gold); }
  .back-headline .line-two .accent { font-weight: 600; }
  .back-rule {
    position: absolute; top: 93px; left: 75px; width: 255px; height: 1px;
    background: linear-gradient(90deg, transparent, var(--gold-line), transparent);
  }
  .back-copy {
    position: absolute; left: 42px; width: 330px;
    font-size: 10.8px; line-height: 12.6px; color: var(--text);
  }
  .back-copy p + p { margin-top: 4px; }
  .copy-intro { top: 107px; }
  .copy-position { top: 185px; }
  .copy-position .book-name {
    color: var(--gold-soft); font-weight: 600; font-size: 12.5px; line-height: 15px;
  }
  .learn-heading {
    position: absolute; top: 268px; left: 42px;
    font-size: 13px; font-weight: 600; color: var(--gold-soft);
  }
  .outcomes { position: absolute; left: 42px; top: 296px; width: 330px; list-style: none; }
  .outcome { position: relative; padding-left: 22px; font-size: 9.6px; line-height: 11.5px; }
  .outcome + .outcome { margin-top: 11px; }
  .outcome svg { position: absolute; left: 0; top: 1px; width: 10px; height: 10px; }
  .outcome-title { display: block; color: var(--gold-soft); font-weight: 600; }
  .closing-quote {
    position: absolute; top: 453px; left: 36px; width: 340px;
    text-align: center; font-style: italic; font-size: 12.4px; line-height: 14.8px;
  }
  .closing-quote .mark { color: var(--gold); }
  .author-block { position: absolute; left: 42px; top: 528px; }
  .author-block .author { font-size: 15.5px; font-weight: 600; color: var(--white); line-height: 1.1; }
  .author-block .website { font-size: 10px; font-style: italic; color: var(--gold); }
  .barcode-space {
    position: absolute; left: 265px; top: 516px; width: 110px; height: 59px;
    background: var(--white);
  }

  /* ---------- Spine ---------- */
  .spine {
    position: relative; width: 28px; height: 100%;
    background: linear-gradient(180deg, #1a2444, #111831 60%, #0c1226);
    font-family: 'Barlow Condensed', sans-serif; text-transform: uppercase;
  }
  .spine-title, .spine-hook {
    position: absolute; left: 50%; transform: translateX(-50%);
    writing-mode: vertical-rl; white-space: nowrap; color: var(--white);
  }
  .spine-title { top: 40px; font-size: 15.5px; font-weight: 500; letter-spacing: 0.2px; }
  .spine-hook { top: 416px; font-size: 10.5px; font-weight: 500; }

  /* ---------- Front cover ---------- */
  .front {
    position: relative; width: 404px; height: 100%; overflow: hidden;
    background:
      radial-gradient(ellipse 60% 40% at 50% 20%, rgba(60,80,130,0.35), transparent 70%),
      linear-gradient(180deg, var(--navy-mid) 0%, var(--navy) 50%, var(--navy-deep) 100%);
    color: var(--white);
  }
  .growth-art {
    position: absolute; left: 0; right: 0; top: 150px; bottom: 0;
    background:
      radial-gradient(ellipse 28% 50% at 88% 42%, rgba(240,190,60,0.55), transparent 70%),
      radial-gradient(ellipse 60% 28% at 58% 70%, rgba(200,150,50,0.35), transparent 70%),
      radial-gradient(ellipse 50% 18% at 50% 95%, rgba(160,120,50,0.22), transparent 70%);
  }
  .front-rule {
    position: absolute; left: 64px; width: 268px; height: 1px;
    background: linear-gradient(90deg, transparent, var(--gold-line) 20%, var(--gold-line) 80%, transparent);
  }
  .rule-a { top: 19px; } .rule-b { top: 47px; } .rule-c { top: 203px; } .rule-d { top: 252px; }
  .kicker {
    position: absolute; top: 26px; left: 0; width: 100%; text-align: center;
    font-family: 'Poppins', sans-serif; font-weight: 500;
    font-size: 11px; letter-spacing: 3.3px; color: var(--white);
  }
  .front-title {
    position: absolute; top: 62px; left: 0; width: 100%; text-align: center;
    font-family: 'Barlow Condensed', sans-serif; font-weight: 700;
    text-transform: uppercase; line-height: 1;
  }
  .front-title .t1 { display: block; font-size: 44px; }
  .front-title .t2 { display: block; font-size: 48px; color: var(--gold); margin-top: 2px; }
  .front-title .t3 {
    display: flex; align-items: center; justify-content: center; gap: 10px;
    font-size: 37px; margin-top: 1px;
  }
  .dash { display: inline-block; width: 32px; height: 2px; background: var(--gold); }
  .front-subtitle {
    position: absolute; top: 210px; left: 0; width: 100%; text-align: center;
    font-family: 'Poppins', sans-serif; font-size: 12.8px; line-height: 17px;
    text-transform: uppercase; color: var(--text);
  }
  .front-hook {
    position: absolute; top: 504px; left: 0; width: 100%; text-align: center;
    font-family: 'Barlow Condensed', sans-serif; font-weight: 600;
    font-size: 19px; color: var(--white);
  }
  .front-author {
    position: absolute; top: 553px; left: 0; width: 100%;
    display: flex; align-items: center; justify-content: center; gap: 18px;
    font-family: 'Barlow Condensed', sans-serif; font-weight: 700;
    font-size: 23px; color: var(--gold-soft);
  }
  .front-author .dash { width: 40px; }
</style>
</head>
<body>
<main class="wrap">

  <section class="back">
    <h2 class="back-headline">
      <div class="line-one">Is your <span class="accent">software company</span></div>
      <div class="line-two"><span class="accent">Ready</span> for a high-value exit?</div>
    </h2>
    <div class="back-rule"></div>

    <div class="back-copy copy-intro">
      <p>Selling a software company is a high-stakes, complex process—one that can determine the <span class="accent">financial</span> outcome for founders, investors and stakeholders.</p>
      <p>Yet most businesses enter a sale process underprepared, leaving millions in value on the table.</p>
    </div>

    <div class="back-copy copy-position">
      <p><span class="book-name">Grooming Your Platform Firm Toward Purchase</span><br>is a practical, execution-focused playbook for founders, CFOs and boards navigating the M&amp;A process.</p>
      <p>It provides a clear framework to prepare your business, position it for buyers, and maximise valuation.</p>
    </div>

    <h3 class="learn-heading">Inside, you’ll learn how to:</h3>
    <ul class="outcomes">
      <li class="outcome">
        <svg viewBox="0 0 20 20" aria-hidden="true"><circle cx="10" cy="10" r="8.5" fill="none" stroke="var(--gold-soft)" stroke-width="1.6"/><path d="M6 10.3l2.8 2.7L14.3 7.5" fill="none" stroke="var(--gold-soft)" stroke-width="1.8" stroke-linecap="round" stroke-linejoin="round"/></svg>
        <span class="outcome-title">Maximise Valuation</span>Optimise financials, KPIs and growth narrative to attract premium offers
      </li>
      <li class="outcome">
        <svg viewBox="0 0 20 20" aria-hidden="true"><circle cx="10" cy="10" r="8.5" fill="none" stroke="var(--gold-soft)" stroke-width="1.6"/><path d="M6 10.3l2.8 2.7L14.3 7.5" fill="none" stroke="var(--gold-soft)" stroke-width="1.8" stroke-linecap="round" stroke-linejoin="round"/></svg>
        <span class="outcome-title">Prepare for Due Diligence</span>Avoid the most common issues that derail deals
      </li>
      <li class="outcome">
        <svg viewBox="0 0 20 20" aria-hidden="true"><circle cx="10" cy="10" r="8.5" fill="none" stroke="var(--gold-soft)" stroke-width="1.6"/><path d="M6 10.3l2.8 2.7L14.3 7.5" fill="none" stroke="var(--gold-soft)" stroke-width="1.8" stroke-linecap="round" stroke-linejoin="round"/></svg>
        <span class="outcome-title">Navigate the M&amp;A Process</span>Understand buyers, advisors and deal dynamics
      </li>
      <li class="outcome">
        <svg viewBox="0 0 20 20" aria-hidden="true"><circle cx="10" cy="10" r="8.5" fill="none" stroke="var(--gold-soft)" stroke-width="1.6"/><path d="M6 10.3l2.8 2.7L14.3 7.5" fill="none" stroke="var(--gold-soft)" stroke-width="1.8" stroke-linecap="round" stroke-linejoin="round"/></svg>
        <span class="outcome-title">Position for Private Equity &amp; Strategic Buyers</span>Align your business with what acquirers actually value
      </li>
    </ul>

    <p class="closing-quote"><span class="mark">“</span>Whether you’re planning an exit in 12 months or 3 years, this book provides the structure and insight needed to achieve a successful outcome.<span class="mark">”</span></p>

    <div class="author-block">
      <div class="author">Author Name</div>
      <div class="website">Website (optional)</div>
    </div>
    <div class="barcode-space"></div>
  </section>

  <section class="spine">
    <div class="spine-title">Grooming your <span class="accent">platform firm</span> toward purchase</div>
    <div class="spine-hook">Maximise valuation. Navigate M&amp;A.</div>
  </section>

  <section class="front">
    <div class="growth-art" role="img" aria-label="Glowing gold rising bar chart with an upward arrow over a dim city skyline"></div>
    <div class="front-rule rule-a"></div>
    <div class="kicker">A PRACTICAL M&amp;A PLAYBOOK</div>
    <div class="front-rule rule-b"></div>

    <h1 class="front-title">
      <span class="t1">Grooming your</span>
      <span class="t2">Platform firm</span>
      <span class="t3"><span class="dash"></span>Toward purchase<span class="dash"></span></span>
    </h1>

    <div class="front-rule rule-c"></div>
    <p class="front-subtitle">The Platform Harvest Manual<br>for Founders, CFOs &amp; Boards</p>
    <div class="front-rule rule-d"></div>

    <p class="front-hook">MAXIMISE VALUATION. NAVIGATE M&amp;A.</p>
    <div class="front-author"><span class="dash"></span>AUTHOR NAME<span class="dash"></span></div>
  </section>

</main>
</body>
</html>
```